Commercial Refrigeration Service Company requires stylish and fresh looking flyer.

We need a flyer to hand out to new customers. It should have a photo and our branding, list all the services that are offered and our contact details.
We would like two flyers to be supplied, both identical though one offering a discount until July ( Half Price Service Fee ). The flyer should be clear, interesting and in similar colours to the branding package supplied.
Please look at our website for information about the services on offer:
www.frostvale-cooling.com.au

Target Market(s)

Cafes, bars, restaurants, pubs ect.

Font styles to use
Other font styles liked:
• Font package provided

Colors
85cae6
ffffff
333333

Requirements
Must have
• - The photo provided.
• - The company logo.
• - Similar feel to the website & business card.
• - Smooth layout and clear to understand.
Should not have
• - No clunky badges or prints.

```html
<!DOCTYPE html>
<html lang="en">
<head>
<meta charset="utf-8">
<title>Frostvale Cooling – Service Flyers</title>
<link rel="stylesheet" href="https://fonts.googleapis.com/css2?family=Montserrat:wght@400;500;600&family=Questrial&display=swap">
<style>
  :root {
    --brand-blue: #85cae6;
    --accent-blue: #4fc0ee;
    --ink: #333333;
    --white: #ffffff;
    --panel-grey: #999a9c;
    --footer-dark: #333335;
    --backdrop: #e4e5e6;
  }
  * { box-sizing: border-box; margin: 0; padding: 0; }
  html, body { width: 1200px; height: 830px; overflow: hidden; }
  body { background: var(--backdrop); position: relative; font-family: "Questrial", sans-serif; color: var(--ink); }

  .flyer {
    position: absolute; top: 42px; width: 510px; height: 723px;
    background: var(--white); overflow: hidden;
    box-shadow: 0 4px 10px rgba(0,0,0,.25);
  }
  .flyer--discount { left: 53px; }
  .flyer--standard { left: 638px; }
  .flyer > * { position: absolute; }

  .hero-photo {
    left: 0; top: 0; width: 510px; height: 252px;
    background: linear-gradient(180deg, #9fb4c4 0%, #7d8b97 28%, #5e6770 55%, #6c6f73 78%, #8a8a88 100%);
  }
  .rule { left: 0; width: 510px; height: 3px; background: var(--accent-blue); }
  .rule--top { top: 252px; }
  .rule--mid { top: 447px; }
  .rule--low { top: 649px; }

  .intro {
    left: 0; top: 255px; width: 510px; height: 192px;
    background: linear-gradient(90deg, #d9d9da 0%, #ffffff 30%, #ffffff 70%, #d6d6d7 100%);
  }
  .brand-panel {
    left: 30px; top: 271px; width: 188px; height: 52px;
    background: var(--brand-blue);
    display: flex; align-items: center; justify-content: center;
    font-family: "Montserrat", sans-serif; font-weight: 500;
    font-size: 15px; letter-spacing: 5px; color: var(--ink);
  }
  .headline {
    left: 246px; top: 268px;
    font-family: "Montserrat", sans-serif; font-weight: 600;
    font-size: 14.2px; letter-spacing: 1.3px; line-height: 19.8px; color: var(--ink);
  }
  .tagline {
    left: 246px; top: 376px; margin-top: -42px;
    font-family: "Montserrat", sans-serif; font-weight: 500;
    font-size: 11.6px; letter-spacing: 1.1px; color: var(--accent-blue);
  }
  .about {
    left: 30px; top: 371px; width: 454px;
    font-size: 9.5px; line-height: 11.7px; text-align: justify; color: var(--ink);
  }

  .services { left: 0; top: 450px; width: 510px; height: 199px; background: var(--panel-grey); }
  .services-title {
    left: 0; top: 462px; width: 510px; text-align: center;
    font-family: "Montserrat", sans-serif; font-weight: 500;
    font-size: 15px; letter-spacing: 2px; color: var(--accent-blue);
  }
  .services-divider { left: 113px; top: 486px; width: 284px; height: 1px; background: #c9cacc; }

  .service { width: 120px; margin-left: -60px; text-align: center; color: var(--white); font-size: 8.2px; }
  .service svg { display: block; margin: 0 auto 4px; width: 34px; height: 36px; }
  .service svg * { fill: none; stroke: var(--white); stroke-width: 1.4; stroke-linecap: round; stroke-linejoin: round; }

  .footer { left: 0; top: 652px; width: 510px; height: 71px; background: var(--footer-dark); }

  .offer {
    left: 30px; top: 638px; width: 188px; height: 85px; background: var(--accent-blue);
    color: var(--white); text-align: center;
    font-family: "Montserrat", sans-serif; font-weight: 500;
  }
  .offer-line { position: absolute; left: 0; width: 100%; font-size: 10.6px; letter-spacing: 1.6px; }
  .offer-line--top { top: 13px; }
  .offer-dots { position: absolute; left: 0; width: 100%; top: 32px; font-size: 7px; letter-spacing: 6px; }
  .offer-line--bottom { top: 56px; font-weight: 600; }

  .contact-stack {
    left: 246px; top: 658px; color: var(--white);
    font-family: "Montserrat", sans-serif; font-size: 9px; letter-spacing: 1px; line-height: 12.4px;
  }
  .web {
    font-family: "Montserrat", sans-serif; font-weight: 500;
    font-size: 9.2px; letter-spacing: 2.4px; color: var(--accent-blue);
  }
  .web--discount { left: 246px; top: 702px; }
  .web--standard { left: 0; width: 510px; text-align: center; top: 702px; }

  .contact-line {
    left: 0; top: 673px; width: 510px; text-align: center; color: var(--white);
    font-family: "Montserrat", sans-serif; font-size: 11.6px; letter-spacing: 1.6px; white-space: nowrap;
  }
  .contact-line .sep { color: var(--accent-blue); font-size: 7px; margin: 0 7px; vertical-align: 2px; }
</style>
</head>
<body>

<svg width="0" height="0" style="position:absolute" aria-hidden="true">
  <defs>
    <symbol id="icon-thermometer" viewBox="0 0 34 36">
      <path d="M14 4 a3 3 0 0 1 6 0 v19 a6 6 0 1 1 -6 0 z"/><path d="M17 12 v14"/><path d="M23 6h4M23 10h3M23 14h4M23 18h3"/>
    </symbol>
    <symbol id="icon-ice" viewBox="0 0 34 36">
      <path d="M6 4 h22 l-3 28 h-16 z"/><path d="M6 11 h22"/><rect x="11" y="15" width="6" height="6"/><rect x="17" y="20" width="6" height="6"/><rect x="12" y="23" width="5" height="5"/>
    </symbol>
    <symbol id="icon-tap" viewBox="0 0 34 36">
      <path d="M24 3 l4 3 -8 10"/><path d="M8 16 h16 v6 h-16 z"/><path d="M20 22 v4 h-4"/><path d="M18 30 v2"/>
    </symbol>
    <symbol id="icon-bolt" viewBox="0 0 34 36">
      <path d="M20 2 l-10 18 h8 l-4 14 l12 -20 h-8 l6 -12 z"/>
    </symbol>
    <symbol id="icon-tools" viewBox="0 0 34 36">
      <path d="M6 8 a5 5 0 0 0 6 6 l14 14 2 -2 -14 -14 a5 5 0 0 0 -6 -6 l3 3 -2 2 z"/><path d="M28 6 l-12 12"/><path d="M14 20 l-6 6 2 2 6 -6"/>
    </symbol>
    <symbol id="icon-cart" viewBox="0 0 34 36">
      <path d="M1 6 h5 l3 18 h20 l3 -14 h-24"/><circle cx="12" cy="29" r="2"/><circle cx="26" cy="29" r="2"/>
    </symbol>
    <symbol id="icon-ruler" viewBox="0 0 34 36">
      <path d="M4 10 l6 -6 22 22 -6 6 z"/><path d="M13 7 l-2 2M17 11 l-2 2M21 15 l-2 2M25 19 l-2 2"/><path d="M28 6 l-20 20 -3 5 5 -3 20 -20 z"/>
    </symbol>
  </defs>
</svg>

<!-- Flyer with July discount -->
<article class="flyer flyer--discount">
  <div class="hero-photo" role="img" aria-label="Photo of the technician leaning on the company service ute by the beach"></div>
  <div class="rule rule--top"></div>
  <div class="intro"></div>
  <div class="brand-panel">FROSTVALE</div>
  <p class="headline">COMMERCIAL REFRIGERATION<br>&amp; ELECTRICAL SERVICES.<br>ICE MAKERS &amp; BEER SYSTEMS</p>
  <p class="tagline">24 Hr Service, Sales &amp; Installations</p>
  <p class="about">Frostvale Cooling is a company based in Eastern Sydney, providing commercial refrigeration and electrical services. Daniel and his team believe in developing tight relationships with their clients and keeping things simple by offering a personalised service - speak to the same people and see the same faces. Frostvale is completely paperless and uses cloud based trade service software to build a complete profile of your venue and equipment, allowing Daniel to offer tailored advice for your business.</p>
  <div class="rule rule--mid"></div>
  <section class="services"></section>
  <h2 class="services-title">OUR SERVICES</h2>
  <div class="services-divider"></div>
  <div class="service" style="left:81px;top:508px"><svg><use href="#icon-thermometer"/></svg>Commercial Refrigeration</div>
  <div class="service" style="left:199px;top:508px"><svg><use href="#icon-ice"/></svg>Ice makers</div>
  <div class="service" style="left:317px;top:508px"><svg><use href="#icon-tap"/></svg>Beer Systems</div>
  <div class="service" style="left:435px;top:508px"><svg><use href="#icon-bolt"/></svg>Electrical</div>
  <div class="service" style="left:132px;top:575px"><svg><use href="#icon-tools"/></svg>24hr Service</div>
  <div class="service" style="left:258px;top:575px"><svg><use href="#icon-cart"/></svg>Sales</div>
  <div class="service" style="left:384px;top:575px"><svg><use href="#icon-ruler"/></svg>Installations</div>
  <div class="rule rule--low"></div>
  <footer class="footer"></footer>
  <div class="offer">
    <span class="offer-line offer-line--top">DISCOUNT UNTIL JULY</span>
    <span class="offer-dots">◆◆◆</span>
    <span class="offer-line offer-line--bottom">HALF PRICE SERVICE FEE</span>
  </div>
  <p class="contact-stack">DANIEL HARLOW<br>0400 118 274<br>info@frostvale-cooling.com.au</p>
  <p class="web web--discount">WWW.FROSTVALE-COOLING.COM.AU</p>
</article>

<!-- Standard flyer -->
<article class="flyer flyer--standard">
  <div class="hero-photo" role="img" aria-label="Photo of the technician leaning on the company service ute by the beach"></div>
  <div class="rule rule--top"></div>
  <div class="intro"></div>
  <div class="brand-panel">FROSTVALE</div>
  <p class="headline">COMMERCIAL REFRIGERATION<br>&amp; ELECTRICAL SERVICES.<br>ICE MAKERS &amp; BEER SYSTEMS</p>
  <p class="tagline">24 Hr Service, Sales &amp; Installations</p>
  <p class="about">Frostvale Cooling is a company based in Eastern Sydney, providing commercial refrigeration and electrical services. Daniel and his team believe in developing tight relationships with their clients and keeping things simple by offering a personalised service - speak to the same people and see the same faces. Frostvale is completely paperless and uses cloud based trade service software to build a complete profile of your venue and equipment, allowing Daniel to offer tailored advice for your business.</p>
  <div class="rule rule--mid"></div>
  <section class="services"></section>
  <h2 class="services-title">OUR SERVICES</h2>
  <div class="services-divider"></div>
  <div class="service" style="left:81px;top:508px"><svg><use href="#icon-thermometer"/></svg>Commercial Refrigeration</div>
  <div class="service" style="left:199px;top:508px"><svg><use href="#icon-ice"/></svg>Ice makers</div>
  <div class="service" style="left:317px;top:508px"><svg><use href="#icon-tap"/></svg>Beer Systems</div>
  <div class="service" style="left:435px;top:508px"><svg><use href="#icon-bolt"/></svg>Electrical</div>
  <div class="service" style="left:132px;top:575px"><svg><use href="#icon-tools"/></svg>24hr Service</div>
  <div class="service" style="left:258px;top:575px"><svg><use href="#icon-cart"/></svg>Sales</div>
  <div class="service" style="left:384px;top:575px"><svg><use href="#icon-ruler"/></svg>Installations</div>
  <div class="rule rule--low"></div>
  <footer class="footer"></footer>
  <p class="contact-line">DANIEL HARLOW<span class="sep">◆</span>0400 118 274<span class="sep">◆</span>info@frostvale-cooling.com.au</p>
  <p class="web web--standard">WWW.FROSTVALE-COOLING.COM.AU</p>
</article>

</body>
</html>
```